Smoke Into Sanctuary How America's Most Infamous Strip Club Became a Church.

This compelling story deserves a great cover which conveys transformation. As a pastor, I started a church in the financial district of Atlanta. What began as a typical "church plant" became an adventure in risk, creativity, and the building was a beautiful metaphor of transformation as we took a closed down strip club and turned it into a church venue. Our group learned many lessons about accepting people from all sorts of backgrounds, and about seeing God's power at work. I envision a cover which communicates transformation, perhaps using darkness and light, or maybe using the Ruby Lounge building being painted. It was a solid black building (with gold trim) and we painted it white, with a blue logo of the church name. I need book cover, spine, and back, along with whatever is needed for Brisklane to accept it for their site.

```html
<!DOCTYPE html>
<html lang="en">
<head>
<meta charset="utf-8">
<title>Smoke Into Sanctuary – Cover Wrap</title>
<link rel="stylesheet" href="https://fonts.googleapis.com/css2?family=Montserrat:wght@400;500;600;700;800&family=Mrs+Saint+Delafield&display=swap">
<style>
  :root {
    --page: #ffffff;
    --mist: #eceeee;
    --mist-dark: #d9dcdc;
    --peach: #f3c7b4;
    --title-brown: #6e3a2c;
    --accent-red: #d62b33;
    --ink: #222222;
    --muted: #555555;
    --white: #ffffff;
    --night: #141010;
    --plum: #5a2a3a;
  }
  * { box-sizing: border-box; margin: 0; padding: 0; }
  html, body { width: 1200px; height: 2266px; overflow: hidden; background: var(--page); }
  body { position: relative; font-family: "Montserrat", sans-serif; }

  .cover-wrap {
    position: absolute; left: 80px; top: 125px; width: 1032px; height: 715px; overflow: hidden;
    background:
      radial-gradient(ellipse 260px 420px at 0% 90%, rgba(243,199,180,.85), transparent 70%),
      radial-gradient(ellipse 300px 200px at 100% 0%, rgba(150,160,160,.55), transparent 70%),
      radial-gradient(ellipse 400px 300px at 40% 30%, var(--white), transparent 70%),
      linear-gradient(180deg, var(--mist), var(--mist-dark));
  }

  .cover-photo {
    position: absolute; left: 474px; top: 330px; width: 558px; height: 385px;
    background:
      radial-gradient(ellipse 240px 120px at 55% 25%, rgba(255,255,255,.9), transparent 75%),
      radial-gradient(ellipse 180px 110px at 95% 60%, rgba(120,50,70,.85), transparent 75%),
      linear-gradient(180deg, rgba(236,238,238,0) 0%, rgba(200,200,200,.4) 35%, var(--plum) 58%, var(--night) 78%, var(--night) 100%);
  }

  /* title lockup */
  .title-lockup { position: absolute; text-align: center; color: var(--title-brown); font-weight: 800; line-height: .86; letter-spacing: -1px; }
  .title-lockup .script { display: block; font-family: "Mrs Saint Delafield", cursive; font-weight: 400; letter-spacing: 0; color: var(--ink); }
  .title-lockup .big { display: block; text-transform: uppercase; }

  .front-title { left: 553px; width: 479px; top: 110px; }
  .front-title .big.first { font-size: 96px; }
  .front-title .script.link { font-size: 52px; height: 30px; line-height: 30px; }
  .front-title .big.second { font-size: 60px; }

  .back-title { left: 0; width: 474px; top: 128px; }
  .back-title .big.first { font-size: 52px; }
  .back-title .script.link { font-size: 28px; height: 16px; line-height: 16px; }
  .back-title .big.second { font-size: 33px; }

  /* front text */
  .front-tagline { position: absolute; left: 553px; width: 479px; top: 536px; text-align: center; }
  .tagline-top { color: var(--white); font-size: 19px; font-weight: 500; }
  .tagline-band { display: inline-block; margin-top: 6px; background: var(--accent-red); color: var(--white); font-size: 19px; font-weight: 500; padding: 1px 8px; }
  .front-rule { position: absolute; left: 755px; top: 624px; width: 74px; height: 2px; background: var(--accent-red); }
  .front-author { position: absolute; left: 553px; width: 479px; top: 643px; text-align: center; color: var(--white); font-size: 23px; font-weight: 700; letter-spacing: .5px; }

  /* spine */
  .spine {
    position: absolute; left: 474px; width: 79px; top: 66px; height: 600px;
    writing-mode: vertical-rl; display: flex; align-items: center; gap: 14px;
  }
  .spine-subtitle { display: flex; flex-direction: column; align-items: flex-start; font-size: 12.5px; font-weight: 500; color: var(--ink); }
  .spine-subtitle .band { background: var(--accent-red); color: var(--white); padding: 3px 1px; margin-top: 3px; }
  .spine-title { font-weight: 800; color: var(--title-brown); font-size: 19px; line-height: .9; text-align: center; }
  .spine-title .small { font-size: 13px; }
  .spine-dash { width: 2px; height: 14px; background: var(--accent-red); writing-mode: horizontal-tb; }
  .spine-author { font-size: 15px; font-weight: 700; color: var(--ink); letter-spacing: .5px; }

  /* back */
  .back-copy { position: absolute; left: 42px; width: 410px; top: 268px; font-size: 12px; line-height: 16.5px; color: var(--ink); }
  .back-copy p { margin-bottom: 9px; }
  .author-bio { position: absolute; left: 40px; top: 480px; width: 400px; display: flex; gap: 7px; }
  .author-image { flex: 0 0 83px; height: 87px; background: var(--white); display: flex; align-items: center; justify-content: center; text-align: center; font-size: 10px; line-height: 12px; color: var(--ink); }
  .author-bio p { font-size: 12px; line-height: 16.5px; color: var(--ink); }
  .isbn-box { position: absolute; left: 290px; top: 595px; width: 148px; height: 74px; background: var(--white); display: flex; align-items: center; justify-content: center; font-size: 12px; color: var(--muted); }
</style>
</head>
<body>
  <section class="cover-wrap" aria-label="Full book cover wrap">
    <div class="cover-photo" role="img" aria-label="Photo of a wooden cross before bright church windows, a man in a suit raising his arms, and a crowd with warm lights below"></div>

    <!-- back cover -->
    <h2 class="title-lockup back-title">
      <span class="big first">Smoke</span>
      <span class="script link">into</span>
      <span class="big second">Sanctuary</span>
    </h2>
    <div class="back-copy">
      <p>Lorem Ipsum is simply dummy text of the printing and typesetting industry. Lorem Ipsum has been the industry's standard dummy text ever since the 1500s, when an Lorem Ipsum passags, and more recently with desktop pubng software like Inkwell Layout includi versions of Lorem Ipsum.</p>
      <p>Lorem Ipsum is simply dummy text of the printing and typesetting industry. Lorem Ipsum has been the industry's standard dummy text ever since the 1500s, when an Lorem Ipsum passags, and more recently with desktop pubng software like Inkwell Layout includi versions of Lorem Ipsum. Lorem Ipsum is simply dummy text of the printing and typesetting industry.</p>
    </div>
    <div class="author-bio">
      <div class="author-image">author<br>image</div>
      <p>Lorem Ipsum is simply dummy text of the printing and typesetting industry. Lorem Ipsum has been the industry's standard dummy text ever since the 1500s, when an Lorem Ipsum passags, and more recently with desktop pubng software like Inkwell Layout includi versions of Lorem Ipsum.</p>
    </div>
    <div class="isbn-box">ISBN</div>

    <!-- spine -->
    <div class="spine">
      <div class="spine-subtitle">
        <span>How America's Most Infamous</span>
        <span class="band">Strip Club Became a Church.</span>
      </div>
      <div class="spine-title">SMOKE<br><span class="small">INTO</span><br>SANCTUARY</div>
      <span class="spine-dash"></span>
      <div class="spine-author">AUTHOR NAME</div>
    </div>

    <!-- front cover -->
    <h1 class="title-lockup front-title">
      <span class="big first">Smoke</span>
      <span class="script link">into</span>
      <span class="big second">Sanctuary</span>
    </h1>
    <div class="front-tagline">
      <div class="tagline-top">How America's Most Infamous</div>
      <div class="tagline-band">Strip Club Became a Church.</div>
    </div>
    <div class="front-rule"></div>
    <div class="front-author">AUTHOR NAME</div>
  </section>
</body>
</html>
```